Roll up/retractable banner for trade show - higher education software company

My company, BrightQuill Scholastics, will be attending a trade show soon, and we need a design for a "roll up" or "retractable" banner. According to the printer, it must be exactly 33 inches wide by 81 inches tall, at a DPI of 150 (not 300).

This is the exact product from Zorvena: https://zrvn.example/8Kq2LmPx

The banner should have a professional feel and have a similar aesthetic to our brochure, web site, etc. Please see attached files. Use as much or as little as you see fit from the attached files. If you use stock photos in your design, just let me know where I need to go to purchase them.

Our software company focuses on advising and student success for colleges and universities. I like the idea of focusing on the "use cases" of our software, rather than specific software offerings, but I am open to interpretations.

Website: https://brightquillscholastics.example

REQUIREMENT
The final product MUST be in a file format which I can edit later on, with elements in different layers. Either Photoshop or GIMP will be fine, though I can also load .ai files. GIMP is actually preferred, but not required. Mainly, I must be able to alter text, move graphics around, swap out graphics, etc, as needed in the future. If you only work with psd and ai, please provide both file versions in the end.

Target Market(s)

University staff / VP's / presidents / decision-makers at trade shows and conferences

Industry/Entity Type

Higher Education / Software Development

Font styles to use
Sans Serif
Other font styles liked:
• MONTSERRAT is the font used in my logo and brochure, I use RALEWAY on the website. But these are not requirements-- Use what you think looks best.

Requirements
Must have
• 33"wide by 81" tall, 150 DPI. Professional appearance. Final files must be PSD, AI, or GIMP format so I can edit/tweak text and images later if needed. If using AI, please provide both .ai and .psd files.
Nice to have
• Similar wording/content/graphics/colors & fonts as brochure and website (see attached files). Especially some of the use-case wording from the brochure. Flashy and important information should be at the top of the banner, because if this is placed behind a table in a booth, info on the bottom might be obscured or hidden. The QR code from the brochure might be nice to have as well.

```html
<!DOCTYPE html>
<html lang="en">
<head>
<meta charset="utf-8">
<title>BrightQuill Scholastics – Roll-up Banner</title>
<link href="https://fonts.googleapis.com/css2?family=Montserrat:wght@400;500;600;700;800&display=swap" rel="stylesheet">
<style>
  :root {
    --orange: #ef8a23;
    --blue: #1f8fc4;
    --pink: #d93a78;
    --ink: #1d1d1f;
    --page: #ececec;
    --white: #ffffff;
    --photo-light: #eef0f2;
    --photo-mid: #b8bcc2;
    --photo-dark: #5a6270;
  }
  * { margin: 0; padding: 0; box-sizing: border-box; }
  html, body { width: 800px; height: 1200px; overflow: hidden; background: var(--page); }
  body { font-family: "Montserrat", sans-serif; position: relative; }

  .banner {
    position: absolute; left: 168px; top: 30px;
    width: 464px; height: 1140px;
    background: var(--white); overflow: hidden;
    box-shadow: 0 2px 10px rgba(0,0,0,0.08);
  }

  .brand {
    position: absolute; top: 52px; left: 0; width: 100%;
    display: flex; justify-content: center; align-items: center; gap: 10px;
  }
  .brand-mark { width: 26px; height: 26px; background: var(--orange); }
  .brand-name { font-size: 19px; font-weight: 600; color: var(--ink); letter-spacing: 0.5px; }

  .headline { position: absolute; top: 116px; left: 0; width: 100%; text-align: center; }
  .headline span {
    display: block; font-weight: 800; text-transform: uppercase;
    font-size: 27px; line-height: 31px; letter-spacing: 0.3px;
  }
  .headline .orange { color: var(--orange); }
  .headline .blue { color: var(--blue); }

  .team-photo {
    position: absolute; top: 236px; left: 0; width: 464px; height: 460px;
    background: linear-gradient(180deg, var(--photo-light) 0%, var(--photo-mid) 35%, var(--photo-dark) 55%, var(--photo-mid) 80%, var(--white) 100%);
  }
  .shapes { position: absolute; top: 0; left: 0; }

  .devices {
    position: absolute; top: 585px; left: 58px; width: 386px; height: 185px;
    background: linear-gradient(180deg, #4a4d52 0%, #dfe3e8 40%, #f4f6f8 100%);
    border-radius: 4px;
  }

  .tagline {
    position: absolute; top: 792px; left: 0; width: 100%; text-align: center;
    font-size: 16px; font-weight: 600; line-height: 19px; color: var(--ink);
  }
  .tagline em { font-style: normal; color: var(--pink); }

  .facts {
    position: absolute; top: 862px; left: 36px; width: 393px; height: 118px;
    border: 1px solid #b9bcc0; border-top: none; border-radius: 0 0 6px 6px;
  }
  .facts::before, .facts::after {
    content: ""; position: absolute; top: 0; height: 1px; width: 50px; background: #b9bcc0;
  }
  .facts::before { left: 0; } .facts::after { right: 0; }
  .facts-title {
    position: absolute; top: 846px; left: 76px; width: 312px; height: 30px;
    background: var(--orange); color: var(--white);
    clip-path: polygon(0 0, 100% 0, 94% 100%, 6% 100%);
    border-radius: 0 0 8px 8px;
    text-align: center; font-size: 17px; font-weight: 500; line-height: 30px; text-transform: uppercase;
  }
  .fact {
    position: absolute; top: 903px; width: 118px; height: 77px; border-radius: 8px;
    color: var(--white); font-size: 15px; font-weight: 700; text-align: center; padding-top: 35px;
  }
  .fact.powerful { left: 47px; background: var(--pink); }
  .fact.flexible { left: 173px; background: var(--orange); text-transform: uppercase; font-size: 13px; }
  .fact.hassle-free { left: 300px; background: var(--blue); text-transform: uppercase; font-size: 13px; }
  .fact-icon {
    position: absolute; top: -18px; left: 39px; width: 40px; height: 40px; border-radius: 50%;
    background: var(--white); border: 4px solid; display: flex; align-items: center; justify-content: center;
  }
  .powerful .fact-icon { border-color: var(--blue); }
  .flexible .fact-icon { border-color: var(--pink); }
  .hassle-free .fact-icon { border-color: var(--orange); }

  .call-label {
    position: absolute; top: 992px; left: 0; width: 100%; text-align: center;
    color: var(--pink); font-size: 25px; font-weight: 700; text-transform: uppercase;
  }
  .phone {
    position: absolute; top: 1020px; left: 0; width: 100%;
    display: flex; justify-content: center; align-items: center; gap: 8px;
    font-size: 34px; font-weight: 700; color: var(--ink);
  }
  .phone-icon { width: 32px; height: 32px; }

  .footer {
    position: absolute; bottom: 0; left: 0; width: 100%; height: 70px; background: var(--blue);
    color: var(--white); font-size: 17px; font-weight: 700; text-align: center; line-height: 66px;
  }
</style>
</head>
<body>
  <main class="banner">
    <div class="brand">
      <span class="brand-mark"></span>
      <span class="brand-name">BrightQuill Scholastics</span>
    </div>

    <h1 class="headline">
      <span class="orange">Academic Advising</span>
      <span class="blue">Early Alerts</span>
      <span class="orange">Text Messaging</span>
      <span class="blue">Appointments &amp; More</span>
    </h1>

    <div class="team-photo" role="img" aria-label="Photo of three business people meeting around a laptop at a glass table in a bright office"></div>

    <svg class="shapes" width="464" height="800" viewBox="0 0 464 800" aria-hidden="true">
      <polygon points="464,480 318,618 464,572" fill="var(--orange)"/>
      <polygon points="326,632 464,584 464,700 392,730" fill="var(--blue)"/>
      <polygon points="0,655 47,586 104,648 82,650 47,612 0,684" fill="var(--pink)"/>
      <rect x="0" y="735" width="464" height="65" fill="var(--white)"/>
    </svg>

    <div class="devices" role="img" aria-label="Software screens shown on a desktop monitor, tablet, phone and laptop"></div>

    <p class="tagline">We focus on the <em>"use cases"</em> in our software<br>for better user experience</p>

    <div class="facts"></div>
    <div class="facts-title">Facts about service</div>

    <div class="fact powerful">
      <span class="fact-icon">
        <svg width="18" height="18" viewBox="0 0 24 24"><path d="M13 2 4 14h7l-1 8 9-12h-7z" fill="none" stroke="#222" stroke-width="2" stroke-linejoin="round"/></svg>
      </span>Powerful
    </div>
    <div class="fact flexible">
      <span class="fact-icon">
        <svg width="18" height="18" viewBox="0 0 24 24"><path d="M4 7h16M4 12h16M4 17h16" stroke="#222" stroke-width="2" stroke-linecap="round"/></svg>
      </span>Flexible
    </div>
    <div class="fact hassle-free">
      <span class="fact-icon">
        <svg width="18" height="18" viewBox="0 0 24 24"><circle cx="12" cy="12" r="9" fill="none" stroke="#222" stroke-width="2"/><path d="M8 12l3 3 5-6" fill="none" stroke="#222" stroke-width="2" stroke-linecap="round"/></svg>
      </span>Hassle-free
    </div>

    <div class="call-label">Call us at</div>
    <div class="phone">
      <svg class="phone-icon" viewBox="0 0 32 32" aria-hidden="true">
        <circle cx="16" cy="16" r="16" fill="var(--orange)"/>
        <path d="M11 8c1 0 2 3 2 4s-1.5 1.5-1.5 2.5 3 5 5 5.5c1 0 1.5-1.5 2.5-1.5s4 1 4 2-1.5 3.5-3.5 3.5C14 24 8 18 8 12c0-2 2-4 3-4z" fill="var(--white)"/>
      </svg>
      <span>555-014-2297</span>
    </div>

    <footer class="footer">www.brightquillscholastics.example</footer>
  </main>
</body>
</html>
```